Chutney and Jam Manufacturer needs a label for Jar.

We would like a label designed for a new Christmas Jars called Barnabys Big Fire Pickle and Nollys Dawn Cordial. The retailers we are targeting are Garden Centres, farm shops and independent retail. Although in some ways not relevant some of the Christmas beer labels carry some form of theme we are looking for. Its fun and festive and not an all year around serious product. That said please note our target market.
The label will be approximately 90mm wide x 55mm height.
Picture of the Jar provided.

Target Market(s)

Predominantly female 40+ due to outlet supplied. But this is not paramount to the design.

Industry/Entity Type

Home And Garden

Requirements
Must have
• Clear design on shelf of what it is - remember this is to go on glass jars.
• Shelf impact and clarity
• The design feel is in the name of the product. Barnabys Big Fire Pickle and Nollys Dawn Cordial
Nice to have
• Fun and quirky but again not essential.
Should not have
• The Brand is Wexley Foods but this is not important on this concept. We will add in the logo if we have room and it fits in with the selected design.

```html
<!DOCTYPE html>
<html lang="en">
<head>
<meta charset="utf-8">
<title>Barnabys Big Fire Pickle – Jar Label</title>
<link href="https://fonts.googleapis.com/css2?family=Playfair+Display:wght@400;700;900&display=swap" rel="stylesheet">
<style>
  :root {
    --page: #f2f2f2;
    --cream: #f4efe2;
    --cream-deep: #ece5d3;
    --gold: #d8b27a;
    --red: #c8202a;
    --red-dark: #7e0f14;
    --red-light: #d82a30;
    --green-dark: #1f6a1c;
    --green-light: #8cc63f;
    --stripe-white: #f6f1e4;
  }
  html, body {
    margin: 0;
    padding: 0;
    width: 1163px;
    height: 1200px;
    overflow: hidden;
    background: var(--page);
  }
  .label {
    position: absolute;
    left: 51px;
    top: 72px;
    width: 1060px;
    height: 1055px;
    display: flex;
    flex-direction: column;
    box-shadow: 0 10px 30px rgba(0,0,0,0.15);
  }
  .label__panel {
    position: relative;
    height: 686px;
    overflow: hidden;
    background: radial-gradient(ellipse at 40% 40%, var(--cream) 0%, var(--cream-deep) 100%);
  }
  .label__gold-rule { height: 6px; background: var(--gold); }
  .label__band {
    height: 264px;
    background: linear-gradient(100deg, var(--red) 0%, var(--red-dark) 45%, var(--red-light) 100%);
  }
  .label__white-rule { height: 5px; background: var(--stripe-white); }
  .label__green-stripe {
    height: 94px;
    background: linear-gradient(90deg, var(--green-dark) 0%, var(--green-light) 100%);
  }
  .title {
    position: absolute;
    inset: 0;
    margin: 0;
    font-family: "Playfair Display", Georgia, serif;
    font-weight: 400;
  }
  .title__cap {
    position: absolute;
    left: 110px;
    top: -22px;
    font-size: 620px;
    line-height: 1;
    font-weight: 700;
    color: var(--red);
  }
  .title__green {
    background: linear-gradient(90deg, var(--green-dark) 0%, var(--green-light) 100%);
    -webkit-background-clip: text;
    background-clip: text;
    color: transparent;
  }
  .title__line {
    position: absolute;
    left: 505px;
    white-space: nowrap;
    line-height: 1;
  }
  .title__line--first {
    top: 126px;
    font-size: 120px;
    font-weight: 400;
  }
  .title__line--second {
    top: 276px;
    font-size: 110px;
    font-weight: 400;
    color: var(--red);
  }
  .title__line--third {
    top: 398px;
    font-size: 175px;
    font-weight: 700;
  }
</style>
</head>
<body>
  <div class="label">
    <div class="label__panel">
      <h1 class="title" aria-label="Barnabys Big Fire Pickle">
        <span class="title__cap" aria-hidden="true">B</span>
        <span class="title__line title__line--first title__green" aria-hidden="true">arnabys</span>
        <span class="title__line title__line--second" aria-hidden="true">Big Fire</span>
        <span class="title__line title__line--third title__green" aria-hidden="true">Pickle</span>
      </h1>
    </div>
    <div class="label__gold-rule"></div>
    <div class="label__band"></div>
    <div class="label__white-rule"></div>
    <div class="label__green-stripe"></div>
  </div>
</body>
</html>
```